Wordpress Design For Financial Investment Company

//** NEW WIREFRAME ADDED TO HELP WITH LAYOUT ISSUES. PLEASE REFER TO WIREFRAME IN ATTACHED FILES. NO DESIGN WILL BE CONSIDERED IF IT DOES NOT FOLLOW THE WIREFRAME. **//
//** PLEASE READ THE ENTIRE BRIEF INCLUDING ALL UPDATES TO THE BRIEF. THE CLIENT IS VERY SPECIFIC ABOUT WHAT THEY WANT AND I'VE COVERED SEVERAL THINGS IN THE UPDATES. THERE IS ALSO A VIDEO UPDATE THAT HAS SOME VALUABLE INFORMATION IN IT FOR THIS CONTEST. **//
The client is an investment advisor who needs a new website designed. The current site is http://www.velmorfield.net.
The client wants the site to be green to match the attached logo.
The home page should have relevant images in the rotator. No people hugging! This is a financial investment site, not a family counseling site.
Also, the client wants 4 buttons on the home page to highlight the 4 main areas they focus on:
Investment Advice and Education
General Financial Planning
Retirement Planning
401K Planning
The top right area of the site needs to have their phone number, a call to action, and 2 buttons.
Their phone number is 303-418-7639
The call to action should say something like "Call for a free consultation!"
The buttons need to say:
Login To Your Bluvexa Account
Login To Your Quillbrook Account
The final design should communicate professionalism, financial safety and growth.
Main navigation should be:
Home
About Us
Associates
Services
Contact
Mission Statement (Could also be "Our Mission")
This is a site that the client likes: http://www.pwkinvestmentconsulting.com/
Updates
The designs should not have:
Newsletter content. A newsletter sign up is fine
Learning Center
Calculators
Stock prices/tickers
The design should have a contact form on the page.
I have talked to my client and have some updates. I did a video update because I thought it would be easier to show what I'm trying to get across.
Reason: I am going to be extending the contest a few more days. I'm still not getting quite what I want and very few people are even trying to follow the creative brief and the updates to it.
PLEASE read the entire brief and the updates. There is also a video I made that explains everything. I've also attached a wireframe.
Thanks!
Target Market(s)
People looking for a high-end financial investment company.
Industry/Entity Type
Investment
Requirements
Must have
- !!FOLLOW THE WIREFRAME FOR LAYOUT!!
!!THEIR LOGO!!
4 buttons to highlight their main practice areas
Phone number in the top right
"Free Consultation" call to action
2 Login buttons in the top right
A contact form on the page.
Should not have
- The designs should not have:
Learning Center
Calculators
Stock prices/tickers

```html
<!DOCTYPE html>
<html lang="en">
<head>
<meta charset="utf-8">
<title>Velmorfield Financial</title>
<link rel="stylesheet" href="https://fonts.googleapis.com/css2?family=Arimo:wght@400;700&display=swap">
<style>
:root{
  --green:#2b5c42;
  --green-light:#3d7a58;
  --orange:#f7941d;
  --orange-dark:#e27a0c;
  --page:#dcdcdc;
  --band:#ebebee;
  --white:#ffffff;
  --ink:#333333;
  --muted:#555555;
  --line:#d0d0d0;
  --footer:#4a4a4a;
}
*{box-sizing:border-box;margin:0;padding:0}
html,body{width:847px;height:1200px;overflow:hidden}
body{background:var(--page);font-family:"Arimo",Arial,sans-serif;color:var(--ink);position:relative}
.abs{position:absolute}
.container-top{left:62px;top:0;width:723px;height:470px;background:var(--white)}
.band{left:0;top:470px;width:847px;height:137px;background:var(--band)}
.content{left:62px;top:607px;width:723px;height:452px;background:var(--white)}
.footer{left:62px;top:1059px;width:723px;height:134px;background:var(--footer);color:#fff;text-align:center}

.login-bar{left:437px;top:0;width:348px;height:25px;background:#444;border-radius:0 0 0 6px}
.login-btn{top:4px;height:18px;background:linear-gradient(var(--orange),var(--orange-dark));color:#fff;font-size:9px;line-height:18px;text-align:center;border-radius:2px;white-space:nowrap}

.brand{left:73px;top:50px;display:flex;align-items:center;gap:10px}
.brand-mark{width:22px;height:22px;border-radius:50%;background:var(--green)}
.brand-name{font-size:26px;font-weight:700;color:var(--green)}
.tagline{left:160px;top:106px;font-size:7.5px;font-style:italic;color:#444}

.ask{left:558px;top:33px;width:158px;height:50px}
.ask-text{left:566px;top:37px;color:#fff;line-height:1}
.ask-text b{display:block;font-size:17px;margin-bottom:3px}
.ask-text span{display:block;font-size:12px}
.phone{left:558px;top:84px;font-size:23px;font-weight:700;color:#222;line-height:24px}
.contact-lines{left:560px;top:109px;font-size:11px;line-height:14px;color:#222}
.contact-lines span{display:inline-block;width:40px}

.nav{left:62px;top:136px;width:723px;height:34px;background:var(--green);display:flex}
.nav a{color:#fff;text-decoration:none;font-size:12.5px;padding:0 14px;line-height:34px;border-right:1px solid #3f7258}
.search{left:570px;top:141px;width:138px;height:23px;background:#fff;border-radius:2px;font-size:10.5px;line-height:23px;padding-left:8px;color:#333}

.slider{left:69px;top:176px;width:709px;height:276px;background:#fff;border:1px solid var(--line);border-radius:4px;box-shadow:0 6px 10px rgba(0,0,0,.15)}
.slide-photo{left:74px;top:181px;width:462px;height:264px;background:linear-gradient(120deg,#f4e9d2,#d9b89a 45%,#c9c0b0 70%,#eef0e6)}
.slide-caption{left:74px;top:366px;width:460px;height:56px;background:rgba(90,90,90,.6);color:#fff;font-size:15px;line-height:56px;padding-left:8px;white-space:nowrap;overflow:hidden}
.slide-caption b{font-size:30px;vertical-align:middle;margin-right:2px}
.slide-title{left:548px;top:206px;width:220px;text-align:center;font-size:21px;font-weight:700;color:var(--green);line-height:25px}
.slide-body{left:547px;top:272px;width:200px;font-size:11px;line-height:15px;color:#222}
.btn{background:linear-gradient(#fcb042,var(--orange-dark));color:#fff;text-align:center;border-radius:3px;white-space:nowrap}
.consult{left:585px;top:376px;width:126px;height:34px;line-height:34px;font-size:12px;color:#5a2d00;border-radius:4px;box-shadow:0 3px 4px rgba(0,0,0,.2)}
.dots{left:404px;top:457px;display:flex;gap:3px}
.dots i{width:8px;height:8px;border-radius:50%;background:#bbb}
.dots i:first-child{background:var(--orange)}

.welcome-title{left:88px;top:485px;font-size:18px;color:#222}
.welcome-body{left:88px;top:522px;width:430px;font-size:9.5px;line-height:12.5px;color:#222}
.read{height:16px;line-height:16px;font-size:9px;width:52px}
.newsletter{left:555px;top:484px;width:223px;height:110px;background:var(--green-light);color:#fff}
.newsletter-head{height:32px;background:var(--green);font-size:16px;line-height:32px;padding-left:12px}
.newsletter p{font-size:10px;text-align:center;margin-top:12px}
.nl-input{left:565px;top:556px;width:144px;height:21px;background:#fff;color:#444;font-size:9.5px;line-height:21px;padding-left:6px}
.nl-btn{left:713px;top:556px;width:58px;height:21px;line-height:21px;font-size:10px;font-weight:700;border-radius:0}

.card{top:621px;width:171px;height:158px;background:linear-gradient(#fff 75%,#ececec);border:1px solid var(--line);border-radius:4px;box-shadow:0 6px 8px rgba(0,0,0,.12)}
.card h3{font-size:12px;font-weight:400;text-align:center;margin-top:15px;color:#222;white-space:nowrap}
.card .thumb{position:absolute;left:9px;top:44px;width:54px;height:54px;border:1px solid #ccc}
.card p{position:absolute;left:70px;top:40px;width:95px;font-size:8px;line-height:10.5px;color:#333}
.card .read{position:absolute;right:16px;top:128px}

.about{left:69px;top:800px;width:466px;height:143px;border:1px solid var(--line);border-radius:4px}
.about h2{font-size:14px;font-weight:400;margin:8px 0 0 12px}
.about-photo{left:82px;top:841px;width:136px;height:84px}
.about p{position:absolute;left:166px;top:36px;width:288px;font-size:9.5px;line-height:12.2px}
.testi-title{left:79px;top:961px;font-size:11px}
.testi-arrows{left:505px;top:965px}
.testi{left:69px;top:984px;width:466px;height:52px;background:#eeeeee}
.testi p{position:absolute;left:40px;top:8px;width:400px;font-size:9.5px;line-height:12px}
.testi .who{position:absolute;right:40px;top:32px;font-size:10.5px}
.quote{font-size:34px;color:#cfcfcf;font-family:Georgia,serif}

.quick{left:555px;top:800px;width:223px;height:245px;background:#f5f5f5;border:1px solid var(--line)}
.quick-head{height:32px;background:var(--green);color:#fff;font-size:14px;font-weight:700;line-height:32px;padding-left:12px}
.q-label{left:566px;font-size:10px}
.q-field{left:617px;width:147px;height:20px;background:#fff;border:1px solid #c8c8c8}
.q-btn{left:709px;top:1013px;width:55px;height:18px;line-height:18px;font-size:9.5px;border-radius:2px}

.footer-links{top:9px;width:100%;font-size:9px;white-space:nowrap}
.follow{left:0;top:50px;width:100%;font-size:10.5px;display:flex;justify-content:center;align-items:center;gap:4px}
.follow i{width:16px;height:16px;background:#6d8fbf;border-radius:2px}
.follow i:last-child{background:var(--orange)}
.copyright{top:112px;width:100%;font-size:9.5px}
</style>
</head>
<body>
<div class="abs container-top"></div>
<div class="abs band"></div>
<div class="abs content"></div>

<div class="abs login-bar"></div>
<div class="abs login-btn" style="left:477px;width:141px">Login to your Bluvexa account</div>
<div class="abs login-btn" style="left:630px;width:144px">Login to your Quillbrook account</div>

<div class="abs brand"><span class="brand-mark"></span><span class="brand-name">Velmorfield Financial</span></div>
<div class="abs tagline">"Always do right. This will gratify some people &amp; astonish the rest."</div>

<svg class="abs ask" viewBox="0 0 158 50"><path d="M0 3a3 3 0 0 1 3-3h155l-14 40H30l-8 10-2-10H3a3 3 0 0 1-3-3z" fill="#f7941d"/></svg>
<div class="abs ask-text"><b>Any questions?</b><span>Call Us &nbsp;&nbsp;&nbsp;:</span></div>
<div class="abs phone">303 - 418 - 7639</div>
<div class="abs contact-lines"><span>Fax</span>: 303 - 418 - 7640<br><span>Email</span>: Info@velmorfield.com</div>

<nav class="abs nav"><a>Home</a><a>About Us</a><a>Associates</a><a>Services</a><a>Contact</a><a>Our Mission</a></nav>
<div class="abs search">Site Search</div>
<svg class="abs" style="left:685px;top:144px" width="18" height="17" viewBox="0 0 18 17"><circle cx="7" cy="7" r="5" fill="none" stroke="#222" stroke-width="2"/><path d="M11 11l5 5" stroke="#222" stroke-width="3"/></svg>

<div class="abs slider"></div>
<div class="abs slide-photo" role="img" aria-label="Photo of a smiling retired couple"></div>
<div class="abs slide-caption"><b>50%</b> of retirees left the workforce ealier than planned.</div>
<div class="abs slide-title">Get your question answered!</div>
<div class="abs slide-body">For a free phone consultation, please Click Here. let us know the best dates and times you are available and leave your phone number. If you prefer to contact us, please let us know the date you would like to call.</div>
<div class="abs btn consult">Free Consultation</div>
<svg class="abs" style="left:63px;top:296px" width="32" height="32" viewBox="0 0 32 32"><circle cx="16" cy="16" r="15" fill="#5b3a22"/><path d="M19 9l-7 7 7 7" fill="none" stroke="#fff" stroke-width="3"/></svg>
<svg class="abs" style="left:752px;top:296px" width="32" height="32" viewBox="0 0 32 32"><circle cx="16" cy="16" r="15" fill="#5b3a22"/><path d="M13 9l7 7-7 7" fill="none" stroke="#fff" stroke-width="3"/></svg>
<div class="abs dots"><i></i><i></i><i></i><i></i></div>

<h1 class="abs welcome-title" style="font-weight:400">Welcome!</h1>
<p class="abs welcome-body">Lorem ipsum dolor sit amet, consectetuer adipiscing elit, sed diem nonummy nibh euismod tincidunt ut laoreet dolor magna aliquam erat volutpat. ut wisi enim ad minim veniam. Nemo enim ipsam voluptatem quia voluptas sit aspernatur aut odit aut fugit, sed quia consequuntur....</p>
<div class="abs btn read" style="left:462px;top:568px">Read more</div>

<div class="abs newsletter"><div class="newsletter-head">Newsletter Sign Up</div><p>Receive update news from us biweekly</p></div>
<div class="abs nl-input">E-mail Address</div>
<div class="abs btn nl-btn">SUBMIT</div>

<div class="abs card" style="left:69px"><h3>Investment Advice &amp; Education</h3><div class="thumb" style="background:linear-gradient(#9fb2c8,#e6ddd2)" role="img" aria-label="Photo of advisors at a desk"></div><p>Lorem ipsum dolor sit amet, consectetuer adipiscing elit, sed diem nonummy nibh euismod tincidunt ut laoreet dolor magna aliquam erat volutpat. ut wisi enim ad minim veniam</p><div class="btn read">Read more</div></div>
<div class="abs card" style="left:248px"><h3>General financial Planning</h3><div class="thumb" style="background:linear-gradient(#c9d4dc,#8a8f95)" role="img" aria-label="Photo of a client meeting"></div><p>Lorem ipsum dolor sit amet, consectetuer adipiscing elit, sed diem nonummy nibh euismod tincidunt ut laoreet dolor magna aliquam erat volutpat. ut wisi enim ad minim veniam</p><div class="btn read">Read more</div></div>
<div class="abs card" style="left:427px"><h3>Retirement Planning</h3><div class="thumb" style="background:linear-gradient(#a9bfd6,#d8c6b4)" role="img" aria-label="Photo of a retired couple reviewing papers"></div><p>Lorem ipsum dolor sit amet, consectetuer adipiscing elit, sed diem nonummy nibh euismod tincidunt ut laoreet dolor magna aliquam erat volutpat. ut wisi enim ad minim veniam</p><div class="btn read">Read more</div></div>
<div class="abs card" style="left:606px"><h3>401K Planning</h3><div class="thumb" style="background:linear-gradient(#eef2e8,#8fae7d)" role="img" aria-label="Illustration of banknotes and coins"></div><p>Lorem ipsum dolor sit amet, consectetuer adipiscing elit, sed diem nonummy nibh euismod tincidunt ut laoreet dolor magna aliquam erat volutpat. ut wisi enim ad minim veniam</p><div class="btn read">Read more</div></div>

<div class="abs about"><h2>About Us</h2><p>Lorem ipsum dolor sit amet, consectetuer adipiscing elit, sed diem nonummy nibh euismod tincidunt ut laoreet dolor magna aliquam erat volutpat. Ut wisi enim veniam.<br>At vero eos et accusamus et justoodio dignisimos ducimus qui blanditis praesintium voluptatum deleniti atque corrupti quos dolores etquas...</p></div>
<div class="abs about-photo" style="background:linear-gradient(#e9ecef,#3a3f46)" role="img" aria-label="Photo of the advisory team"></div>
<div class="abs btn read" style="left:452px;top:914px">Read more</div>

<div class="abs testi-title">What Our Client's Says About Us</div>
<svg class="abs testi-arrows" width="24" height="14" viewBox="0 0 24 14"><path d="M8 2L3 7l5 5M16 2l5 5-5 5" fill="none" stroke="#333" stroke-width="2"/></svg>
<div class="abs testi"><span class="abs quote" style="left:8px;top:0">&ldquo;</span><p>Lorem ipsum dolor sit amet, consectetuer adipiscing elit, set diem nonummy nibh euismod tincidunt ut laoreet dolor magna aliquam erat volutpat.</p><span class="who">Client Name, City</span><span class="abs quote" style="right:8px;top:14px">&rdquo;</span></div>

<div class="abs quick"><div class="quick-head">Quick Contact</div></div>
<div class="abs q-label" style="top:852px">Name</div><div class="abs q-field" style="top:849px"></div>
<div class="abs q-label" style="top:880px">Email</div><div class="abs q-field" style="top:877px"></div>
<div class="abs q-label" style="top:908px">Phone</div><div class="abs q-field" style="top:905px"></div>
<div class="abs q-label" style="top:933px">Message</div><div class="abs q-field" style="top:930px;height:78px"></div>
<div class="abs btn q-btn">SUBMIT</div>

<footer class="abs footer">
  <div class="abs footer-links">Home I About Us I Associates &nbsp;I&nbsp; Services &nbsp;I&nbsp; Our Mission &nbsp;I&nbsp; Investment Advice I General Financial Planning I Retirement Planning I 401K Planning I Latest News I Blogs I Contact</div>
  <div class="abs follow">Follow Us on : &nbsp;<i></i><i></i><i></i><i></i></div>
  <div class="abs copyright">Copyright &copy; 2013. velmorfield.com. All rights reserved.</div>
</footer>
</body>
</html>
```